Legal Journal cover - modern and sylish

We require a cover design for a new, modern and digital legal academic journal. Attached is our logo so you can get an idea of the feel. This academic journal will have several editions per year.Requirements for the cover design:-The feel of the cover is to be modern -In harmony with our logo-While staying uniform and set in its design,

Colors
ec1f27

Requirements
Must have
• 1) Colour. Each edition will use different colours. (So we will need the source files to be able to continue to do this)
• 2) An image section. We would like to be able to put in different image or photo with each edition. So we need to have a section, most likely in the shape of a strip, that can include a different image or photo each edition. This part is where we can put a different image in for each edition. So this section would need to be able to accommodate different types of images. It could be a single square. Or it could be a line (a strip) that an image or images.
• 3) A title for the edition and volume and number. Like this:
• Volume 34, No 2 (2016): Contemporary Issues in Criminal Law
• I have attached a range of journals I found online to serve as inspiration.

```html
<!DOCTYPE html>
<html lang="en">
<head>
<meta charset="UTF-8">
<title>Lex Horizon — Volume 36, no.1 (2019)</title>
<link href="https://fonts.googleapis.com/css2?family=Roboto:wght@500;700&display=swap" rel="stylesheet">
<style>
  :root {
    --brand-red: #ec1f27;
    --ink-grey: #5b6260;
    --paper: #ffffff;
    --photo-dark: #1b1b1b;
    --photo-warm: #6b4a34;
  }
  html, body {
    margin: 0;
    padding: 0;
    overflow: hidden;
    background: var(--paper);
  }
  .cover {
    position: relative;
    width: 1143px;
    height: 1200px;
    background: var(--paper);
    overflow: hidden;
    font-family: "Roboto", Arial, sans-serif;
  }
  .frame-art {
    position: absolute;
    inset: 0;
    width: 1143px;
    height: 1200px;
  }
  .masthead {
    position: absolute;
    left: 70px;
    top: 66px;
    display: flex;
    align-items: center;
    gap: 18px;
  }
  .masthead-mark {
    width: 96px;
    height: 96px;
    border-radius: 50%;
    background: var(--ink-grey);
  }
  .masthead-name {
    font-weight: 500;
    font-size: 44px;
    letter-spacing: 1px;
    color: var(--brand-red);
    line-height: 1;
  }
  .edition-year,
  .edition-number {
    position: absolute;
    right: 35px;
    margin: 0;
    font-weight: 500;
    font-size: 31px;
    color: var(--brand-red);
    line-height: 1;
  }
  .edition-year { top: 290px; }
  .edition-number { top: 430px; }
  .edition-title {
    position: absolute;
    right: 58px;
    top: 972px;
    margin: 0;
    text-align: right;
    font-weight: 500;
    font-size: 43px;
    line-height: 46px;
    color: var(--ink-grey);
    text-transform: uppercase;
  }
</style>
</head>
<body>
<main class="cover">
  <svg class="frame-art" viewBox="0 0 820 860" preserveAspectRatio="none" aria-hidden="false">
    <defs>
      <radialGradient id="photoTone" cx="45%" cy="40%" r="70%">
        <stop offset="0%" stop-color="var(--photo-warm)"/>
        <stop offset="55%" stop-color="#3a2e27"/>
        <stop offset="100%" stop-color="var(--photo-dark)"/>
      </radialGradient>
    </defs>
    <path class="frame-band" fill="var(--brand-red)"
      d="M0,860 L0,380 A140,140 0 0 1 140,240 L820,240 L820,295 L140,295 A85,85 0 0 0 55,380 L55,860 Z"/>
    <circle class="frame-ring" cx="215" cy="435" r="160" fill="var(--brand-red)"/>
    <circle class="photo-border" cx="215" cy="435" r="145" fill="var(--paper)"/>
    <g class="photo-slot" role="img" aria-label="Edition photo: a hand placing wooden letter blocks that spell LAW on a dark background">
      <circle cx="215" cy="435" r="136" fill="url(#photoTone)"/>
    </g>
  </svg>

  <header class="masthead">
    <span class="masthead-mark"></span>
    <span class="masthead-name">LEX HORIZON</span>
  </header>

  <p class="edition-year">2019</p>
  <p class="edition-number">Volume 36, no.1</p>

  <h1 class="edition-title">Lex Horizon<br>for the<br>digital age</h1>
</main>
</body>
</html>
```